Diverse business needs a corporate identity system

Varrow Brisk Holdings Limited is a well established family owned and run business operating in Port Moresby, Papua New Guinea since 1989. As part of taking the business to the next level, we are redoing our branding/corporate identity.

We currently carry out two core business activities servicing corporate clients in the commercial and industrial sectors:
1. Electrical - new installations and maintenance work
2. Construction - mostly commercial & industrial, some residential

We are looking to add the following business activities in near future:
1. IT consulting
2. Property development - business/industrial park, residential complexes, low cost housing
3. Retail of hardware, construction supplies and flat pack furniture & kitchens

We have just completed our logo design here on SketchHarbor and now wanting to design business card and stationery based on our new logo (attached).

Deliverables are:
1. Business card - double sided
2. Letterhead A4

Details to go on the card:
Name: Martin Fenwale
Title: Director
Email: martin.fenwale@varrowbrisk.example
Tel: +675 3481720, +675 3487043
Office: Section 17 Lot 43, Kessaby Light Industrial Area, Port Moresby, Papua New Guinea
Postal: PO Box 914, Kessaby, NCD, Papua New Guinea
Website: varrowbrisk.example

Our services can be listed somewhere on the card:
Electrical, Construction, Property Development, IT Consulting

Details to go on the letterhead:
Varrow Brisk Holdings Ltd.
PO Box 914, Kessaby, NCD, Papua New Guinea
Fax: +675 3486158
Email: info@varrowbrisk.example

For inspiration, I have uploaded some images of business cards we like.

Would be good if the same/similar business card design could be printed both economically (e.g. full coloured both sides, matte card stock) for majority of staff and upscaled to use premium features such as letter pressed, foil etc for use by executives. Otherwise, please provide two separate designs.

Logo text font is nexa bold freefont - please use something from nexa family or another font type that complements it.

Reason: Few designs were submitted. Most were clearly from ready to use templates. No designs really stand out for us at the moment. So we have decided to narrow the focus to just business card and A4 letterhead. And also revised the brief to be completely open to hopefully invite more creative designs.

I have updated the brief to be a lot less restrictive to try and get more creative designs. Also uploaded more images of premium business cards for inspiration.

Construction

Requirements
Must have
• All designs must conform to quillpress specifications. Refer to and download appropriate work file templates from http://www.quillpress.example/uploads/templates.aspx?ref=5820146631&tab=0.
Should not have
• No QR codes and social media links.

```html
<!DOCTYPE html>
<html lang="en">
<head>
<meta charset="utf-8">
<title>Varrow Brisk Holdings – Business Card</title>
<link href="https://fonts.googleapis.com/css2?family=Nunito:wght@400;700;800&display=swap" rel="stylesheet">
<style>
  :root {
    --backdrop: #2b2b2b;
    --card-white: #f4f4f3;
    --brand-red: #c8372b;
    --brand-gold: #e2b21c;
    --text-grey: #777776;
    --card-shadow: rgba(0, 0, 0, 0.45);
  }
  * { margin: 0; padding: 0; box-sizing: border-box; }
  html, body {
    width: 1200px;
    height: 900px;
    overflow: hidden;
  }
  body {
    position: relative;
    background: var(--backdrop);
    font-family: "Nunito", sans-serif;
  }
  .card {
    position: absolute;
    left: 354px;
    width: 488px;
    height: 278px;
    box-shadow: 0 2px 6px var(--card-shadow);
  }
  .card-front { top: 154px; background: var(--card-white); }
  .card-back  { top: 464px; background: var(--brand-red); }

  .front-brand {
    position: absolute;
    left: 27px;
    top: 191px;
    display: flex;
    align-items: center;
    gap: 8px;
  }
  .brand-dot {
    width: 30px;
    height: 30px;
    border-radius: 50%;
    background: var(--brand-red);
  }
  .brand-name {
    font-weight: 800;
    font-size: 25px;
    color: var(--brand-red);
    letter-spacing: -0.2px;
  }

  .contact-block {
    position: absolute;
    left: 270px;
    top: 54px;
    color: var(--text-grey);
    font-size: 13.5px;
    line-height: 17px;
  }
  .person-name {
    font-weight: 800;
    font-size: 14.5px;
    color: var(--brand-red);
    letter-spacing: 0.3px;
  }
  .person-title { margin-bottom: 24px; }
  .contact-line {
    display: flex;
    align-items: center;
    gap: 4px;
    height: 17px;
  }
  .contact-line svg { width: 11px; height: 11px; flex: none; }
  .contact-list { margin-bottom: 28px; }
  .company-name {
    font-weight: 700;
    font-size: 13.5px;
    color: var(--brand-red);
  }

  .back-brand {
    position: absolute;
    left: 0;
    right: 0;
    top: 84px;
    text-align: center;
    font-weight: 800;
    font-size: 44px;
    color: var(--brand-gold);
    letter-spacing: -0.5px;
  }
  .back-web {
    position: absolute;
    left: 0;
    right: 0;
    top: 231px;
    text-align: center;
    font-weight: 700;
    font-size: 13px;
    letter-spacing: 3px;
    color: #ffffff;
  }
</style>
</head>
<body>
  <section class="card card-front">
    <div class="front-brand">
      <span class="brand-dot"></span>
      <span class="brand-name">Varrow Brisk</span>
    </div>
    <div class="contact-block">
      <div class="person-name">MARTIN FENWALE</div>
      <div class="person-title">President</div>
      <div class="contact-list">
        <div class="contact-line">
          <svg viewBox="0 0 11 11" aria-hidden="true"><rect x="3" y="0.5" width="5.5" height="10" rx="1" fill="none" stroke="#c8372b" stroke-width="1.2"/><rect x="4.3" y="2" width="2.9" height="5" fill="#c8372b"/></svg>
          <span>• 321-408-7152</span>
        </div>
        <div class="contact-line">
          <svg viewBox="0 0 11 11" aria-hidden="true"><rect x="0.5" y="2.5" width="10" height="6.5" fill="#c8372b"/><path d="M0.8 2.8 L5.5 6.3 L10.2 2.8" fill="none" stroke="#f4f4f3" stroke-width="0.9"/></svg>
          <span>• martin@varrowbrisk.example</span>
        </div>
      </div>
      <div class="company-name">Varrow Brisk Holdings Ltd.</div>
      <div>Section 17 Lot 43 Kessaby</div>
      <div>Port Moresby, NCD</div>
      <div>Papua New Guinea</div>
    </div>
  </section>

  <section class="card card-back">
    <div class="back-brand">Varrow Brisk</div>
    <div class="back-web">www.varrowbrisk.example</div>
  </section>
</body>
</html>
```